RWT Installations Ltd Business Cards

We need a business card with our business logo. We provide window and door installations on high-rises in west coast British Colombia, Canada.

I would like my business information and details on one side of the card, and the other side the company name with logo

Target Market(s)

General Contractors

Industry/Entity Type

Construction

Contact Information for Business Card

one side i want my company name and logo in the dark theme logo that i provided

Requirements
Must have
• Tomas Verelund, 15559284016, RWTInstallations@mailvera.example, 1408-5192 Pellow Avenue Burnaby BC, V0X 1Z9, Owner & Manager

```html
<!DOCTYPE html>
<html lang="en">
<head>
<meta charset="utf-8">
<title>RWT Installations Ltd – Business Cards</title>
<link rel="stylesheet" href="https://fonts.googleapis.com/css2?family=Montserrat:wght@400;600;700&family=Lato:wght@400&display=swap">
<style>
  :root {
    --scene: #2b2c2e;
    --card-dark: #3a3b3e;
    --card-light: #ffffff;
    --brand-blue: #27a6e0;
    --brand-grey: #8a8a8a;
    --ink-grey: #4a4a4a;
    --text-soft: #555555;
  }
  * { margin: 0; padding: 0; box-sizing: border-box; }
  html, body { width: 1200px; height: 952px; overflow: hidden; }
  body {
    background: var(--scene);
    position: relative;
    font-family: "Lato", sans-serif;
  }
  .card {
    position: absolute;
    top: 331px;
    width: 500px;
    height: 290px;
    border-radius: 18px;
    overflow: hidden;
  }
  .card--front { left: 70px; background: var(--card-dark); }
  .card--back { left: 630px; background: var(--card-light); }

  .accent-tab {
    position: absolute;
    width: 16px;
    height: 112px;
    background: var(--brand-blue);
  }
  .accent-tab--top { left: 0; top: 34px; border-radius: 0 8px 8px 0; }
  .accent-tab--bottom { right: 0; bottom: 34px; border-radius: 8px 0 0 8px; }

  .brand {
    display: flex;
    align-items: center;
    gap: 12px;
  }
  .brand__mark {
    width: 30px;
    height: 30px;
    background: var(--brand-grey);
  }
  .brand__name {
    font-family: "Montserrat", sans-serif;
    font-weight: 600;
    color: var(--brand-blue);
    letter-spacing: 0.02em;
  }
  .card--front .brand {
    position: absolute;
    left: 50%; top: 50%;
    transform: translate(-50%, -50%);
  }
  .card--front .brand__name { font-size: 28px; white-space: nowrap; }

  .card--back .brand { position: absolute; left: 34px; top: 30px; }
  .card--back .brand__mark { width: 22px; height: 22px; }
  .card--back .brand__name { font-size: 19px; }

  .contact-list {
    position: absolute;
    left: 34px;
    top: 110px;
    list-style: none;
    font-size: 11px;
    color: var(--text-soft);
    line-height: 1.35;
  }
  .contact-list li {
    display: flex;
    align-items: flex-start;
    gap: 8px;
    margin-bottom: 7px;
  }
  .contact-icon {
    flex: none;
    width: 14px;
    height: 14px;
    border-radius: 3px;
    background: var(--brand-blue);
    display: flex;
    align-items: center;
    justify-content: center;
  }
  .contact-icon svg { width: 10px; height: 10px; }

  .person {
    position: absolute;
    right: 34px;
    top: 118px;
    text-align: right;
    font-family: "Montserrat", sans-serif;
  }
  .person__name {
    font-size: 20px;
    color: var(--brand-blue);
    letter-spacing: 0.04em;
    font-weight: 400;
  }
  .person__name strong { font-weight: 700; }
  .person__role {
    font-family: "Lato", sans-serif;
    font-size: 13px;
    color: var(--ink-grey);
    margin-top: 2px;
    letter-spacing: 0.03em;
  }
</style>
</head>
<body>

  <section class="card card--front" aria-label="Business card front">
    <span class="accent-tab accent-tab--top"></span>
    <span class="accent-tab accent-tab--bottom"></span>
    <div class="brand">
      <span class="brand__mark"></span>
      <span class="brand__name">RWT Installations Ltd</span>
    </div>
  </section>

  <section class="card card--back" aria-label="Business card back">
    <div class="brand">
      <span class="brand__mark"></span>
      <span class="brand__name">RWT Installations Ltd</span>
    </div>

    <ul class="contact-list">
      <li>
        <span class="contact-icon">
          <svg viewBox="0 0 10 10"><path d="M5 0.8a3 3 0 0 1 3 3c0 2.2-3 5.4-3 5.4S2 6 2 3.8a3 3 0 0 1 3-3z" fill="#fff"/><circle cx="5" cy="3.8" r="1.1" fill="#27a6e0"/></svg>
        </span>
        <span>1408-5192 Pellow Avenue<br>Burnaby BC, V0X 1Z9</span>
      </li>
      <li>
        <span class="contact-icon">
          <svg viewBox="0 0 10 10"><path d="M2.2 1h1.6l.8 2-1 .8a5.5 5.5 0 0 0 2.6 2.6l.8-1 2 .8v1.6c0 .6-.5 1-1.1 1C4.3 8.8 1.2 5.7 1.2 2.1 1.2 1.5 1.6 1 2.2 1z" fill="#fff"/></svg>
        </span>
        <span>15559284016</span>
      </li>
      <li>
        <span class="contact-icon">
          <svg viewBox="0 0 10 10"><rect x="1" y="2.2" width="8" height="5.6" fill="none" stroke="#fff" stroke-width="1"/><path d="M1 2.4l4 3 4-3" fill="none" stroke="#fff" stroke-width="1"/></svg>
        </span>
        <span>RWTInstallations@mailvera.example</span>
      </li>
      <li>
        <span class="contact-icon">
          <svg viewBox="0 0 10 10"><path d="M2.5 1.5l5 3.2-2.2.4 1.3 2.6-1 .5-1.3-2.6-1.6 1.5z" fill="#fff"/></svg>
        </span>
        <span>www.rwtinstallations.example</span>
      </li>
    </ul>

    <div class="person">
      <p class="person__name">TOMAS <strong>VERELUND</strong></p>
      <p class="person__role">Owner &amp; Manager</p>
    </div>
  </section>

</body>
</html>
```